Business Cards for a law firm

Business cards for our law firm. Use our silhoette logo and OAK HARBOR - check our website (www.oakharbor-legal.com)

Contact Information for Business Card

our silhouette logo, OAK HARBOR, 800-555-0147, Dorian Kestrup, dorian@oakharbor-legal.com

Requirements
Must have
• our silhouette logo, OAK HARBOR, 800-555-0147, Dorian Kestrup, dorian@oakharbor-legal.com

```html
<!DOCTYPE html>
<html lang="en">
<head>
<meta charset="utf-8">
<title>Oak Harbor – Business Card</title>
<link rel="stylesheet" href="https://fonts.googleapis.com/css2?family=Cinzel:wght@700&family=Open+Sans:wght@400&display=swap">
<style>
  :root {
    --page: #e4e1dc;
    --navy: #1f2a4d;
    --ink: #3a4560;
    --frost-top: #f4f7fb;
    --frost-mid: #e3ebf3;
    --frost-warm: #efe0df;
    --edge: rgba(90, 100, 120, 0.45);
    --figure: rgba(110, 105, 100, 0.28);
  }
  * { margin: 0; padding: 0; box-sizing: border-box; }
  html, body {
    width: 1200px; height: 970px; overflow: hidden;
    background: var(--page);
  }
  .card {
    position: absolute; left: 100px; top: 200px;
    width: 1000px; height: 568px;
    background:
      radial-gradient(ellipse 320px 160px at 360px 470px, var(--frost-warm), transparent 70%),
      linear-gradient(180deg, var(--frost-top) 0%, var(--frost-mid) 60%, #e9e6e6 100%);
    border: 1px solid var(--edge);
    box-shadow: 0 10px 30px rgba(0,0,0,0.12);
    overflow: hidden;
  }
  .brand-mark {
    position: absolute; left: 53px; top: 80px;
    width: 92px; height: 92px; background: var(--navy);
  }
  .brand-bar {
    position: absolute; left: 53px; top: 223px;
    width: 92px; height: 345px; background: var(--navy);
  }
  .brand-name {
    position: absolute; left: 165px; top: 98px;
    font-family: "Cinzel", serif; font-weight: 700;
    font-size: 46px; letter-spacing: 5px; line-height: 1;
    color: var(--navy);
  }
  .figures-area {
    position: absolute; left: 557px; top: 55px;
    width: 441px; height: 513px;
    background: linear-gradient(180deg, rgba(120,115,110,0.12) 0%, var(--figure) 60%, rgba(120,115,110,0.18) 100%);
  }
  .person-name {
    position: absolute; left: 168px; top: 318px;
    font-family: "Open Sans", sans-serif; font-size: 34px;
    letter-spacing: 1px; color: var(--ink); line-height: 1;
  }
  .contact-list { position: absolute; left: 172px; top: 392px; list-style: none; }
  .contact-item {
    display: flex; align-items: center; height: 39px;
    font-family: "Open Sans", sans-serif; font-size: 27px; color: var(--ink);
  }
  .contact-item svg { width: 18px; height: 18px; margin-right: 14px; fill: var(--ink); flex: none; }
</style>
</head>
<body>
  <section class="card">
    <div class="figures-area" role="img" aria-label="Faint silhouettes of two men in suits standing side by side"></div>
    <div class="brand-mark"></div>
    <div class="brand-bar"></div>
    <h1 class="brand-name">OAK HARBOR</h1>
    <p class="person-name">DORIAN KESTRUP</p>
    <ul class="contact-list">
      <li class="contact-item">
        <svg viewBox="0 0 24 24" aria-hidden="true"><path d="M6.6 10.8c1.4 2.8 3.8 5.1 6.6 6.6l2.2-2.2c.3-.3.7-.4 1-.2 1.1.4 2.3.6 3.6.6.6 0 1 .4 1 1V20c0 .6-.4 1-1 1C10.6 21 3 13.4 3 4c0-.6.4-1 1-1h3.5c.6 0 1 .4 1 1 0 1.3.2 2.5.6 3.6.1.3 0 .7-.2 1z"/></svg>
        800-555-0147
      </li>
      <li class="contact-item">
        <svg viewBox="0 0 24 24" aria-hidden="true"><path d="M2 5h20v14H2z M4 7v.5l8 5 8-5V7l-8 5z" fill-rule="evenodd"/></svg>
        dorian@oakharbor-legal.com
      </li>
      <li class="contact-item">
        <svg viewBox="0 0 24 24" aria-hidden="true"><path d="M12 2a10 10 0 1 0 0 20 10 10 0 0 0 0-20zm0 2c.9 1.2 1.6 2.9 1.9 5h-3.8c.3-2.1 1-3.8 1.9-5zM9.7 4.4C9.1 5.7 8.6 7.3 8.4 9H5a8 8 0 0 1 4.7-4.6zM4.3 11h4c0 .7 0 1.4.1 2H4.3a8 8 0 0 1 0-2zm.7 4h3.4c.2 1.7.7 3.3 1.3 4.6A8 8 0 0 1 5 15zm7 5c-.9-1.2-1.6-2.9-1.9-5h3.8c-.3 2.1-1 3.8-1.9 5zm2.2-7h-4.4c-.1-.7-.1-1.3-.1-2h4.6c0 .7 0 1.3-.1 2zm.1 6.6c.6-1.3 1.1-2.9 1.3-4.6H19a8 8 0 0 1-4.7 4.6zM15.7 13c.1-.6.1-1.3.1-2h4a8 8 0 0 1 0 2zm-.1-4c-.2-1.7-.7-3.3-1.3-4.6A8 8 0 0 1 19 9z"/></svg>
        www.oakharbor-legal.com
      </li>
    </ul>
  </section>
</body>
</html>
```